movie poster Stillwater

Create a movie poster for a thriller/suspense/horror movie called Stillwater which is about a monastery of sinister monks who are hell bent on destroying the world when three friends come on a photography assignment and find they may never escape!

A Marian Holloway Film

Luke Danner -- Adam
Rebecca Thorne -- Alice
Harold Piel -- Cyrus
Dale Amsel --- Brother Giovanni
Beaumont Holloway -- Brother Francesco
Thomas Langree ---Father Cristobal
Frederick Oaten -- Cardinal Barducci
with Harold Vasken --- Gas Station Attendant

Marian Holloway -- Writer, Director, Producer
Stephen Piel -- Director of Photography
Harold Piel -- Special Effects
Stephen Piel -- Editor
Norris "Nudge" Beltrami -- Sound

I just posted an update on the brief for the poster. Please include the credits on your movie poster. Thanks! I will be making a selection in the next few days.

Target Market(s)

This will be a PG and should attract a wide audience

Industry/Entity Type

Movie

Colors
eb1f27

Requirements
Must have
• Movie title, movie credits as provided
All material must be original --- no clip art or material taken from the internet
Nice to have
• tagline
Seeing is believing . . . until you believe what you don't see.

```html
<!DOCTYPE html>
<html lang="en">
<head>
<meta charset="utf-8">
<title>Stillwater — Teaser Poster</title>
<link rel="stylesheet" href="https://fonts.googleapis.com/css2?family=Anton&family=Open+Sans:wght@700&family=Oswald:wght@300;400&display=swap">
<style>
  :root {
    --sky-top: #ee5245;
    --sky-mid: #f26a55;
    --haze: #f7b08f;
    --ember: #d9352c;
    --night: #000000;
    --title-ink: #0c0908;
    --tagline: #ffffff;
    --release-red: #eb1f27;
    --credit-name: #e6dcda;
    --credit-role: #b9312f;
  }
  html, body {
    margin: 0;
    padding: 0;
    width: 761px;
    height: 1200px;
    overflow: hidden;
    background: var(--night);
  }
  .poster {
    position: relative;
    width: 761px;
    height: 1200px;
    overflow: hidden;
    background:
      radial-gradient(ellipse 360px 200px at 50% 520px, var(--haze) 0%, rgba(247,176,143,0) 100%),
      linear-gradient(180deg, var(--sky-top) 0%, var(--sky-mid) 35%, var(--ember) 52%, #7a1b16 62%, var(--night) 74%, var(--night) 100%);
  }
  .scene-art {
    position: absolute;
    left: 0;
    top: 120px;
    width: 761px;
    height: 860px;
  }
  .title {
    position: absolute;
    top: 298px;
    left: 0;
    width: 100%;
    margin: 0;
    text-align: center;
    font-family: "Anton", "Impact", sans-serif;
    font-weight: 400;
    font-size: 132px;
    line-height: 1;
    letter-spacing: 4px;
    color: var(--title-ink);
    text-transform: uppercase;
  }
  .tagline {
    position: absolute;
    top: 478px;
    left: 0;
    width: 100%;
    margin: 0;
    text-align: center;
    font-family: "Open Sans", "Arial", sans-serif;
    font-weight: 700;
    font-size: 20px;
    line-height: 1.5;
    letter-spacing: 3px;
    color: var(--tagline);
    text-transform: uppercase;
  }
  .credits {
    position: absolute;
    top: 842px;
    left: 40px;
    width: 681px;
    text-align: center;
    font-family: "Oswald", "Arial Narrow", sans-serif;
    text-transform: uppercase;
  }
  .credits__presenter {
    margin: 0 0 16px;
    font-weight: 400;
    font-size: 17px;
    letter-spacing: 6px;
    color: var(--credit-name);
  }
  .credits__group {
    display: flex;
    flex-wrap: wrap;
    justify-content: center;
    gap: 8px 26px;
    margin: 0 0 14px;
    padding: 0;
    list-style: none;
  }
  .credit {
    display: flex;
    flex-direction: column;
    align-items: center;
  }
  .credit__name {
    font-weight: 400;
    font-size: 14px;
    letter-spacing: 1.5px;
    line-height: 1.3;
    color: var(--credit-name);
  }
  .credit__role {
    font-weight: 300;
    font-size: 11px;
    letter-spacing: 1.5px;
    line-height: 1.3;
    color: var(--credit-role);
  }
  .release {
    position: absolute;
    top: 1062px;
    left: 0;
    width: 100%;
    margin: 0;
    text-align: center;
    font-family: "Oswald", "Arial Narrow", sans-serif;
    font-weight: 300;
    font-size: 30px;
    letter-spacing: 10px;
    color: var(--release-red);
    text-transform: uppercase;
  }
</style>
</head>
<body>
  <main class="poster">
    <svg class="scene-art" role="img" aria-label="Illustration: ruined skyline in a red haze with power lines, drifting debris and dark ink splatters, and a crowd of hooded figures in silhouette in the foreground" viewBox="0 0 761 860" preserveAspectRatio="none">
      <defs>
        <linearGradient id="crowdShade" x1="0" y1="0" x2="0" y2="1">
          <stop offset="0" stop-color="#000" stop-opacity="0"/>
          <stop offset="0.45" stop-color="#000" stop-opacity="0.85"/>
          <stop offset="1" stop-color="#000" stop-opacity="1"/>
        </linearGradient>
      </defs>
      <rect x="0" y="480" width="761" height="380" fill="url(#crowdShade)"/>
    </svg>

    <h1 class="title">Stillwater</h1>
    <p class="tagline">Seeing is believing . . .<br>until you believe what you don't see.</p>

    <section class="credits" aria-label="Credits">
      <p class="credits__presenter">A Marian Holloway Film</p>
      <ul class="credits__group credits__group--cast">
        <li class="credit"><span class="credit__name">Luke Danner</span><span class="credit__role">Adam</span></li>
        <li class="credit"><span class="credit__name">Rebecca Thorne</span><span class="credit__role">Alice</span></li>
        <li class="credit"><span class="credit__name">Harold Piel</span><span class="credit__role">Cyrus</span></li>
        <li class="credit"><span class="credit__name">Dale Amsel</span><span class="credit__role">Brother Giovanni</span></li>
        <li class="credit"><span class="credit__name">Beaumont Holloway</span><span class="credit__role">Brother Francesco</span></li>
        <li class="credit"><span class="credit__name">Thomas Langree</span><span class="credit__role">Father Cristobal</span></li>
        <li class="credit"><span class="credit__name">Frederick Oaten</span><span class="credit__role">Cardinal Barducci</span></li>
        <li class="credit"><span class="credit__name">with Harold Vasken</span><span class="credit__role">Gas Station Attendant</span></li>
      </ul>
      <ul class="credits__group credits__group--crew">
        <li class="credit"><span class="credit__name">Marian Holloway</span><span class="credit__role">Writer · Director · Producer</span></li>
        <li class="credit"><span class="credit__name">Stephen Piel</span><span class="credit__role">Director of Photography · Editor</span></li>
        <li class="credit"><span class="credit__name">Harold Piel</span><span class="credit__role">Special Effects</span></li>
        <li class="credit"><span class="credit__name">Norris "Nudge" Beltrami</span><span class="credit__role">Sound</span></li>
      </ul>
    </section>

    <p class="release">Coming Soon 2015</p>
  </main>
</body>
</html>
```